Hi, Kimlar Workshop is a Tasmanian based business specialising in fine woodcraft and laser engraving. We produce high quality products using beautiful Tasmanian timbers.We have a logo that we aren't entirely happy with. We don't feel that it stands out or really speaks about who we are as a business. We would like for the new logo to contain the map of Tasmania and perhaps use modern earthy colours in the design to make it pop. The final design should communicate the natural beauty of Tasmanian timbers and the creativity of the artwork. Thank you.

Target Market(s)

They range from souvenir items through to gallery artworks( photos included show some of the different timbers used in the inlay and intarsia pieces.

Industry/Entity Type

Business

Contact Information for Business Card

www.kimlarworkshop.example
email: kimlarworkshop@fernmail.example
Lou Varnesdale of 0455 826 194

Requirements
Must have
• Our logo must have the Map of Tasmania and the words Kimlar Workshop. ( see photo of current logo below) We are open to your ideas of how that could be incorporated into the design.The reverse side of the card would have our email/wesite addresses.. Our website if you need further ideas is www.kimlarworkshop.example and include a phone number for Lou Varnesdale of 0455 826 194
Nice to have
• The font style could reflect elegance and beauty and can be decided by the designer

```html
<!DOCTYPE html>
<html lang="en">
<head>
<meta charset="utf-8">
<title>Kimlar Workshop – Business Card</title>
<link rel="stylesheet" href="https://fonts.googleapis.com/css2?family=Marcellus+SC&family=PT+Sans&display=swap">
<style>
  :root {
    --stage: #3b4247;
    --card: #ffffff;
    --ink: #2b1d1d;
    --maroon: #5e2a2c;
    --body-text: #2f2a2a;
    --faint: #e8e0e0;
    --timber-light: #e7a66a;
    --timber-mid: #d98e4f;
    --timber-dark: #c9783c;
  }
  * { margin: 0; padding: 0; box-sizing: border-box; }
  html, body { width: 1200px; height: 661px; overflow: hidden; }
  body { background: var(--stage); position: relative; font-family: "PT Sans", sans-serif; }

  .card {
    position: absolute; top: 158px; width: 556px; height: 343px;
    background: var(--card); border-radius: 14px; overflow: hidden;
  }
  .card--front { left: 33px; }
  .card--back { left: 610px; }

  .timber-wave { position: absolute; left: 0; top: 0; width: 556px; height: 190px; }

  .brand {
    position: absolute; left: 48px; top: 96px;
    display: flex; align-items: center; gap: 10px;
  }
  .brand__dot { width: 14px; height: 14px; border-radius: 50%; background: var(--maroon); }
  .brand__name { font-family: "Marcellus SC", serif; font-size: 19px; color: var(--maroon); }

  .owner { position: absolute; left: 31px; top: 202px; }
  .owner__name { font-family: "Marcellus SC", serif; font-size: 21px; font-weight: 400; color: var(--ink); letter-spacing: 0.5px; }
  .owner__tagline { font-family: "Marcellus SC", serif; font-size: 16px; color: var(--maroon); margin-top: 1px; letter-spacing: 0.7px; }

  .contact { position: absolute; left: 30px; top: 266px; list-style: none; }
  .contact li { display: flex; align-items: center; gap: 6px; font-size: 14px; color: var(--body-text); line-height: 19px; }
  .contact svg { width: 10px; height: 10px; flex: none; }

  .services { position: absolute; left: 33px; top: 120px; list-style: none; }
  .services li { font-size: 15.5px; color: var(--body-text); line-height: 20.3px; letter-spacing: 0.6px; display: flex; align-items: center; gap: 7px; }
  .services li::before { content: ""; width: 5px; height: 5px; border-radius: 50%; background: var(--maroon); }

  .brand-mark-faint {
    position: absolute; left: 255px; top: 52px; width: 270px; height: 270px;
    border: 3px solid var(--faint); border-radius: 50%;
    display: flex; align-items: flex-start; justify-content: center;
    padding-top: 186px;
  }
  .brand-mark-faint__name { font-family: "Marcellus SC", serif; font-size: 25px; color: var(--faint); }
</style>
</head>
<body>
  <section class="card card--front">
    <svg class="timber-wave" viewBox="0 0 556 190" role="img" aria-label="Tasmanian timber grain texture in warm honey tones">
      <defs>
        <linearGradient id="timber" x1="0" y1="0" x2="1" y2="1">
          <stop offset="0" stop-color="var(--timber-dark)"/>
          <stop offset="0.5" stop-color="var(--timber-light)"/>
          <stop offset="1" stop-color="var(--timber-mid)"/>
        </linearGradient>
      </defs>
      <path d="M0 0 H556 V168 C490 188 410 172 330 116 C250 60 150 18 0 32 Z" fill="url(#timber)"/>
    </svg>

    <div class="brand">
      <span class="brand__dot"></span>
      <span class="brand__name">Kimlar Workshop</span>
    </div>

    <div class="owner">
      <h1 class="owner__name">Lou Varnesdale</h1>
      <p class="owner__tagline">High Quality Woodcraft &amp; Laser Engraving</p>
    </div>

    <ul class="contact">
      <li><svg viewBox="0 0 10 10"><rect x="2.5" y="0.5" width="5" height="9" rx="1" fill="none" stroke="#333" stroke-width="1"/></svg>0455 826 194</li>
      <li><svg viewBox="0 0 10 10"><rect x="0.5" y="2" width="9" height="6" fill="none" stroke="#333" stroke-width="1"/><path d="M0.5 2 L5 5.5 L9.5 2" fill="none" stroke="#333" stroke-width="1"/></svg>kimlarworkshop@fernmail.example</li>
      <li><svg viewBox="0 0 10 10"><circle cx="5" cy="5" r="4.2" fill="none" stroke="#333" stroke-width="1"/><path d="M1 5 H9 M5 1 V9" stroke="#333" stroke-width="0.8"/></svg>www.kimlarworkshop.example</li>
    </ul>
  </section>

  <section class="card card--back">
    <div class="brand-mark-faint">
      <span class="brand-mark-faint__name">Kimlar Workshop</span>
    </div>
    <ul class="services">
      <li>Inlaid &amp; Engraved Timber Products</li>
      <li>Laser Engraving</li>
      <li>Unique Intarsia Designs</li>
      <li>Custom Trophies</li>
      <li>In-house Design &amp; Manufacture</li>
    </ul>
  </section>
</body>
</html>
```